An international online market place website needs a good loook

We are developing an ecomerce platform which supporting the local home business/international suppliers, selling quality products from Jewellery, Kids, Accessory. party goods etc, providing them a reach to a pool of high income individuals. We need a web design. It's targeted to expats in Hong Kong, professional men and women, young families with high disposable income and we'd like to see something modern, chic, clean, welcoming and a feel of community where you can get trusted goods from like-minded people.

Target Market(s)

Expats living in Hong Kong with families or single. Age 28 - 60 with high disposable income. Globe trotting, and international

Industry/Entity Type

Business

Font styles to use
Sans Serif

Colors
85cae6
cadf82
eea4c8

Requirements
Must have
• Log in, Register, Search, What's Trending, Footer - How it works, Search Filter on the left side bar ( Price Bar, Category, Product Type, Delivery Options)

More details see attached file.

```html
<!DOCTYPE html>
<html lang="en">
<head>
<meta charset="utf-8">
<title>Harbourly – Marketplace</title>
<link rel="stylesheet" href="https://fonts.googleapis.com/css2?family=Open+Sans:wght@300;400;600;700&family=PT+Sans+Narrow:wght@400;700&display=swap">
<style>
:root{
  --blue:#85cae6;
  --green:#cadf82;
  --pink:#eea4c8;
  --pink-strong:#e476ad;
  --accent-blue:#4fb6e8;
  --slate:#4b5a5e;
  --ink:#333;
  --light:#f2f2f2;
  --beige:#eeece4;
  --white:#fff;
}
*{box-sizing:border-box;margin:0;padding:0}
html,body{width:1200px;height:2270px;overflow:hidden}
body{position:relative;font-family:"Open Sans",Arial,sans-serif;color:var(--ink);background:var(--white)}
.abs{position:absolute}
.narrow{font-family:"PT Sans Narrow","Arial Narrow",sans-serif}

/* top bar */
.topbar{left:0;top:0;width:1200px;height:38px;background:var(--white)}
.topbar-text{font-size:12px;color:#444;white-space:nowrap}
.currency{left:132px;top:11px;display:flex;align-items:center;gap:8px}
.currency-select{width:95px;height:22px;border:1px solid #ccc;display:flex;align-items:center;gap:6px;padding:0 6px;font-size:11px;margin-top:-3px}
.currency-select .flag{width:16px;height:11px;background:#d9322b}
.account-links{left:652px;top:11px;display:flex;gap:22px}
.account-links span{display:flex;align-items:center;gap:6px}
.cart{left:918px;top:0;width:150px;height:38px;background:var(--blue);color:#fff;display:flex;align-items:center;gap:12px;padding-left:12px;font-size:13px;white-space:nowrap}
.cart b{font-weight:700}

/* header */
.header{left:0;top:38px;width:1200px;height:75px;background:linear-gradient(#fafafa,#e8e8e8)}
.logo{left:132px;top:53px;font-size:33px;font-weight:700;color:#555;letter-spacing:-.5px;line-height:1.2}
.search{left:787px;top:61px;width:281px;height:30px;border:1px solid #ccc;background:#fff;display:flex}
.search span{flex:1;font-size:11px;font-style:italic;color:#888;padding:8px 10px}
.search i{width:32px;background:var(--green);display:flex;align-items:center;justify-content:center}

/* nav */
.nav{left:0;top:113px;width:1200px;height:40px;background:#fff;border-bottom:1px solid #e2e2e2}
.nav ul{position:absolute;left:132px;top:0;display:flex;list-style:none;height:40px}
.nav li{height:40px;display:flex;align-items:center;justify-content:center;font-size:12px;font-weight:600;color:#333;border-right:1px solid #e2e2e2;white-space:nowrap}
.nav li.active{background:var(--blue);color:#fff}

/* hero */
.hero{left:0;top:153px;width:1200px;height:507px;background:radial-gradient(ellipse at 30% 45%,#6b7d80 0%,#4d5c60 60%,#3c484b 100%)}
.hero-photo{left:620px;top:153px;width:580px;height:507px;background:radial-gradient(ellipse at 55% 45%,#d9b7a4 0%,#7a5142 35%,#2c1d19 65%,rgba(60,72,75,0) 90%)}
.hero-copy{left:104px;width:560px;color:#fff;white-space:nowrap;text-align:center}
.hero-kicker{top:341px;height:30px;display:flex;align-items:center;justify-content:center;gap:10px;font-size:16px;font-weight:400}
.hero-kicker hr{flex:0 0 48px;border:0;border-top:2px solid #fff}
.hero-kicker em{font-style:normal;color:var(--accent-blue);font-size:22px}
.hero-title{top:376px;font-size:44px;font-weight:400;line-height:48px;letter-spacing:.3px}
.hero-sub{top:433px;font-size:15px;font-weight:600;line-height:22px}
.hero-btn{left:306px;top:477px;width:155px;height:37px;border-radius:19px;background:var(--pink-strong);color:#fff;font-size:16px;display:flex;align-items:center;justify-content:center;gap:10px;white-space:nowrap}
.hero-btn i{width:14px;height:14px;border-radius:50%;background:#fff;display:inline-block;position:relative}
.hero-btn i:after{content:"";position:absolute;left:5px;top:4px;border-left:5px solid var(--pink-strong);border-top:3px solid transparent;border-bottom:3px solid transparent}
.hero-dots{left:539px;top:613px;width:121px;height:27px;background:rgba(255,255,255,.8);display:flex;align-items:center;justify-content:center;gap:8px}
.hero-dots i{width:9px;height:9px;border-radius:50%;background:#ccc;border:1px solid #aaa}

/* category grid */
.grid-bg{left:0;top:660px;width:1200px;height:941px;background:var(--light)}
.tile{border:1px solid #ddd;background:#fff;overflow:hidden}
.tile .photo{position:absolute;left:0;top:0;width:100%;height:100%}
.tile-label{position:absolute;left:0;height:56px;display:flex;align-items:center;padding-left:18px;font-size:24px;font-weight:700;color:#333;text-transform:uppercase;white-space:nowrap}
.tile-label .go{position:absolute;right:14px;top:19px;width:18px;height:18px;border-radius:50%;background:#444}
.tile-label .go:after{content:"";position:absolute;left:7px;top:5px;border-left:5px solid #fff;border-top:4px solid transparent;border-bottom:4px solid transparent}
.bg-green{background:var(--green)}
.bg-blue{background:var(--blue)}
.bg-pink{background:var(--pink-strong)}
.dad-title{left:30px;top:75px;font-size:42px;font-weight:700;line-height:1.2;color:#333;text-align:center}
.dad-tag{position:absolute;left:8px;bottom:8px;height:32px;padding:0 14px;background:var(--pink-strong);color:#fff;font-size:19px;display:flex;align-items:center;white-space:nowrap}
.small-label{position:absolute;left:0;bottom:0;height:42px;width:188px;display:flex;align-items:center;justify-content:center;font-size:24px;font-weight:700;color:#333;text-transform:uppercase;white-space:nowrap}
.new-ribbon{position:absolute;right:0;top:0}

/* why shop */
.why-tab{left:477px;top:1592px;width:264px;height:42px}
.why-tab span{position:absolute;left:0;top:0;width:264px;height:42px;display:flex;align-items:center;justify-content:center;color:#fff;font-size:21px;font-weight:700}
.why-item{width:260px;text-align:center;font-size:19px;font-weight:600;color:#333;white-space:nowrap}
.why-circle{width:114px;height:114px;border-radius:50%;border:4px solid #3d3d3d;background:#fff;display:flex;align-items:center;justify-content:center}

/* features band */
.features{left:0;top:1879px;width:1200px;height:88px;background:var(--slate)}
.feature{top:1898px;display:flex;align-items:center;gap:12px;color:#fff;white-space:nowrap}
.feature .ring{width:52px;height:52px;border-radius:50%;border:2px solid #fff;display:flex;align-items:center;justify-content:center}
.feature .ring.on{background:var(--blue)}
.feature h4{font-size:18px;font-weight:700;letter-spacing:.5px}
.feature p{font-size:12px;color:#e7ebec}

/* footer */
.footer{left:0;top:1967px;width:1200px;height:257px;background:var(--beige)}
.fcol{top:1997px;font-size:12.5px;color:#333}
.fcol h5{font-size:14px;font-weight:700;text-transform:uppercase;padding-bottom:8px;border-bottom:1px dotted #999;margin-bottom:10px;white-space:nowrap}
.fcol li{list-style:none;line-height:26px;white-space:nowrap}
.about p{font-size:12.5px;line-height:19px;color:#444}
.subscribe-box{display:flex;height:30px;margin-bottom:6px}
.subscribe-box span{flex:1;background:#fff;font-size:11px;padding:8px;color:#444}
.subscribe-box b{width:34px;background:#333;color:#fff;font-size:11px;display:flex;align-items:center;justify-content:center}
.note{font-size:11.5px;font-style:italic;color:#444;line-height:17px}
.socials{display:flex;gap:10px;margin-top:10px}
.socials i{width:27px;height:27px;border-radius:50%;background:#333;display:block}

/* bottom */
.bottom{left:0;top:2224px;width:1200px;height:46px;background:var(--slate)}
.copy{left:133px;top:2239px;color:#dfe4e5;font-size:12px;white-space:nowrap}
.cards{left:820px;top:2236px;display:flex;gap:7px}
.cards i{width:45px;height:26px;background:#f4f4f4;border-radius:2px;border:1px solid #ccc;display:block}
</style>
</head>
<body>

<!-- top bar -->
<div class="abs topbar"></div>
<div class="abs currency topbar-text">Currency :
  <div class="currency-select"><span class="flag"></span>£ GBP
    <svg width="9" height="6" style="margin-left:auto"><path d="M0 0h9L4.5 6z" fill="#888"/></svg></div>
</div>
<div class="abs account-links topbar-text">
  <span><svg width="11" height="11"><circle cx="5.5" cy="3.5" r="3" fill="#444"/><path d="M0 11c0-4 11-4 11 0z" fill="#444"/></svg>My Account</span>
  <span><svg width="10" height="12"><rect y="5" width="10" height="7" fill="#444"/><path d="M2 5V3a3 3 0 016 0v2" stroke="#444" stroke-width="1.6" fill="none"/></svg>Sign in</span>
  <span><svg width="12" height="12"><rect x="0.5" y="2.5" width="9" height="9" fill="none" stroke="#444"/><path d="M4 8l7-7" stroke="#444" stroke-width="2"/></svg>Register</span>
</div>
<div class="abs cart">
  <svg width="26" height="22"><path d="M0 2h5l3 12h14l3-9H7" stroke="#fff" stroke-width="2.4" fill="none"/><circle cx="10" cy="19" r="2.2" fill="#fff"/><circle cx="20" cy="19" r="2.2" fill="#fff"/></svg>
  <span>0 items: <b>$0.00</b></span>
</div>

<!-- header -->
<div class="abs header"></div>
<div class="abs logo">Harbourly</div>
<div class="abs search"><span>Enter search item</span>
  <i><svg width="13" height="13"><circle cx="5.5" cy="5.5" r="4" stroke="#333" stroke-width="2" fill="none"/><path d="M8.5 8.5l4 4" stroke="#333" stroke-width="2"/></svg></i></div>

<!-- nav -->
<nav class="abs nav">
  <ul>
    <li class="active" style="width:90px">GIFTS</li>
    <li style="width:117px">FASHION</li>
    <li style="width:117px">JEWELRY</li>
    <li style="width:133px">CRAFT &amp; ART</li>
    <li style="width:122px">CHILDREN</li>
    <li style="width:144px">FOOD &amp; DRINKS</li>
    <li style="width:100px">HOME</li>
    <li style="width:113px">PARTY</li>
  </ul>
</nav>

<!-- hero -->
<div class="abs hero"></div>
<div class="abs hero-photo" role="img" aria-label="Model with long dark hair wearing a jewelled drop earring"></div>
<div class="abs hero-copy hero-kicker"><hr><span>GET UP TO <em>40% OFF ON</em> SELECTED ITEMS</span><hr></div>
<h1 class="abs hero-copy hero-title">WOMEN'S ACCESSORIES</h1>
<p class="abs hero-copy hero-sub">Lorem ipsum dolaor sit consectetuer adiing elit nibh euismod</p>
<div class="abs hero-btn">SHOP NOW <i></i></div>
<div class="abs hero-dots"><i></i><i></i><i></i><i></i><i></i></div>

<!-- category grid -->
<div class="abs grid-bg"></div>

<div class="abs tile" style="left:132px;top:688px;width:216px;height:215px">
  <div class="photo" role="img" aria-label="Turquoise bead necklace and bracelet on wood" style="background:linear-gradient(135deg,#6a5a4a,#3a8f95 50%,#b49c83)"></div>
  <div class="tile-label bg-green narrow" style="top:159px;width:216px">Jewellery<span class="go"></span></div>
</div>
<div class="abs tile" style="left:372px;top:688px;width:215px;height:215px">
  <div class="photo" role="img" aria-label="Colourful children's toys" style="background:linear-gradient(160deg,#fff 20%,#f0d36a 45%,#e96b3a 65%,#fff 90%)"></div>
  <div class="tile-label bg-green narrow" style="top:159px;width:215px">Kids Zone<span class="go"></span></div>
</div>
<div class="abs tile" style="left:613px;top:688px;width:215px;height:215px">
  <div class="photo" role="img" aria-label="Woman's wrist with gold bangles and handbag" style="background:linear-gradient(120deg,#f2d9b8,#c79a6e 50%,#3b2a22)"></div>
  <div class="tile-label bg-green narrow" style="top:159px;width:215px">Accessory<span class="go"></span></div>
</div>
<div class="abs tile" style="left:853px;top:688px;width:215px;height:215px">
  <div class="photo" role="img" aria-label="Pink party table decorations" style="background:linear-gradient(160deg,#f7eef0,#e7a1b6 45%,#b3334f 75%,#f3e3e7)"></div>
  <div class="tile-label bg-green narrow" style="top:159px;width:215px">Party Goods<span class="go"></span></div>
</div>

<div class="abs tile" style="left:132px;top:927px;width:290px;height:298px">
  <div class="photo" role="img" aria-label="Friends shopping together with bags" style="background:linear-gradient(150deg,#dfe6ea,#b78a8f 45%,#d04a7a 70%,#8aa0b5)"></div>
  <div class="tile-label bg-blue narrow" style="top:253px;width:290px;height:45px">New Sellers
    <span style="position:absolute;right:14px;font-size:17px;font-weight:400;text-transform:none">Find Out More</span></div>
</div>
<div class="abs tile" style="left:445px;top:927px;width:623px;height:298px">
  <div class="photo" role="img" aria-label="Silver charm pendants and a tag on a white surface" style="background:linear-gradient(100deg,#efeeeb 35%,#c9c6c0 65%,#e9e7e2)"></div>
  <div class="abs dad-title narrow">DAD'S TIME<br>TO SHINE</div>
  <div class="dad-tag narrow">Stylish Jewellery and cufflinks for sentiment.</div>
</div>

<div class="abs tile" style="left:132px;top:1253px;width:305px;height:290px">
  <div class="photo" role="img" aria-label="Brown leather travel bag with accessories" style="background:linear-gradient(140deg,#e8e2da,#8b6a4c 45%,#5a4333 65%,#ece6df)"></div>
  <div class="small-label bg-pink narrow">Accessory</div>
</div>
<div class="abs tile" style="left:445px;top:1253px;width:305px;height:290px">
  <div class="photo" role="img" aria-label="Children's denim bag with pink bead handle" style="background:radial-gradient(ellipse at 50% 60%,#7b96b8 0%,#e9a3b6 35%,#fff 65%)"></div>
  <svg class="new-ribbon" width="72" height="72" viewBox="0 0 72 72"><path d="M0 0h30l42 42v30z" fill="#d9143d"/><text x="46" y="26" fill="#fff" font-family="PT Sans Narrow,sans-serif" font-size="15" font-weight="700" transform="rotate(45 46 26)" text-anchor="middle" dominant-baseline="central">NEW</text></svg>
  <div class="small-label bg-green narrow">Children's Bag</div>
</div>
<div class="abs tile" style="left:760px;top:1253px;width:308px;height:290px">
  <div class="photo" role="img" aria-label="Woman wearing a pearl necklace against a sparkling background" style="background:radial-gradient(circle at 60% 50%,#c79c86 0%,#4b3a33 45%,#2a2220 80%)"></div>
  <div class="small-label bg-blue narrow">Jewellery</div>
</div>

<!-- why shop with us -->
<svg class="abs why-tab" viewBox="0 0 264 42"><path d="M0 0h264l-12 34q-4 8-14 8H26q-10 0-14-8z" fill="var(--slate)"/></svg>
<div class="abs why-tab"><span class="narrow">WHY SHOP WITH US</span></div>

<svg class="abs" style="left:330px;top:1690px" width="200" height="40"><path d="M5 30Q90 -5 190 30" stroke="#999" stroke-dasharray="2 3" fill="none"/><path d="M184 22l8 9-11 2" stroke="#999" fill="none"/></svg>
<svg class="abs" style="left:670px;top:1690px" width="200" height="60"><path d="M5 15Q90 60 190 10" stroke="#999" stroke-dasharray="2 3" fill="none"/><path d="M180 6l10 4-6 9" stroke="#999" fill="none"/></svg>

<div class="abs why-circle" style="left:194px;top:1678px"><svg width="52" height="44"><circle cx="16" cy="12" r="7" fill="#5ab1de"/><circle cx="36" cy="12" r="7" fill="#5ab1de"/><circle cx="26" cy="16" r="8" fill="#3a9ed5"/><path d="M2 38c0-14 22-14 22 0zM28 38c0-14 22-14 22 0z" fill="#5ab1de"/><path d="M12 44c0-18 28-18 28 0z" fill="#3a9ed5"/></svg></div>
<div class="abs why-item" style="left:121px;top:1810px">Satisfied Customers</div>

<div class="abs why-circle" style="left:539px;top:1678px"><svg width="56" height="56"><path d="M28 2l6 5 8-1 2 8 7 4-3 8 3 8-7 4-2 8-8-1-6 5-6-5-8 1-2-8-7-4 3-8-3-8 7-4 2-8 8 1z" fill="#a9c93f"/><circle cx="28" cy="28" r="15" fill="none" stroke="#fff" stroke-width="2"/><path d="M20 28l6 6 11-12" stroke="#fff" stroke-width="4" fill="none"/></svg></div>
<div class="abs why-item" style="left:466px;top:1810px">Passionate Sellers</div>

<div class="abs why-circle" style="left:880px;top:1678px"><svg width="40" height="48"><path d="M9 22V14a11 11 0 0122 0v8" stroke="#e476ad" stroke-width="5" fill="none"/><rect y="20" width="40" height="28" rx="3" fill="#e476ad"/><circle cx="20" cy="32" r="4" fill="#fff"/><rect x="18.5" y="33" width="3" height="8" fill="#fff"/></svg></div>
<div class="abs why-item" style="left:807px;top:1810px">Secure Transactions</div>

<!-- features band -->
<div class="abs features"></div>
<div class="abs feature" style="left:133px">
  <div class="ring"><svg width="24" height="24"><path d="M2 12L12 2h10v10L12 22z" fill="#fff"/><circle cx="17" cy="7" r="2" fill="var(--slate)"/></svg></div>
  <div><h4 class="narrow">FEARTURE</h4><p>Lorem ipsum dolor sit amet</p></div>
</div>
<div class="abs feature" style="left:374px">
  <div class="ring on"><svg width="18" height="26"><circle cx="9" cy="9" r="8" fill="#fff"/><rect x="5" y="17" width="8" height="6" fill="#fff"/></svg></div>
  <div><h4 class="narrow">SUPPORT</h4><p>Lorem ipsum dolor sit amet</p></div>
</div>
<div class="abs feature" style="left:616px">
  <div class="ring"><svg width="28" height="18"><rect y="1" width="17" height="12" fill="#fff"/><path d="M18 5h6l4 4v4H18z" fill="#fff"/><circle cx="6" cy="15" r="3" fill="#fff"/><circle cx="22" cy="15" r="3" fill="#fff"/></svg></div>
  <div><h4 class="narrow">FREE SHIPPING</h4><p>Lorem ipsum dolor sit amet</p></div>
</div>
<div class="abs feature" style="left:856px">
  <div class="ring"><svg width="20" height="24"><path d="M4 11V7a6 6 0 0112 0v4" stroke="#fff" stroke-width="3" fill="none"/><rect y="10" width="20" height="14" rx="2" fill="#fff"/></svg></div>
  <div><h4 class="narrow">AFFILIATE</h4><p>Lorem ipsum dolor sit amet</p></div>
</div>

<!-- footer -->
<div class="abs footer"></div>
<div class="abs fcol about" style="left:132px;width:232px">
  <h5>About to Harbourly</h5>
  <p>Morbi sed orci feugiat, laoreet sem in dapibus tellus. Nulla a interdum elit, at porta orci. Nam ultricies mi sit amet orci vehicula rutrum. Cras in sapien quis dui porta molestie. Quisque ut magna eu risus adipiscing sodales. Sed elementum nulla vitae magna venenatis, vel pretium risus auctor.</p>
</div>
<div class="abs fcol" style="left:403px;width:132px">
  <h5>Brands</h5>
  <ul><li>Delivery</li><li>Legal Notice</li><li>About Us</li><li>Secure Payment</li><li>Terms And Conditions</li><li>Career Opportunities</li></ul>
</div>
<div class="abs fcol" style="left:563px;width:112px">
  <h5>Information</h5>
  <ul><li>Specials</li><li>New Products</li><li>Best Sellers</li><li>Our Stores</li><li>Contact Us</li><li>Holiday Shop</li></ul>
</div>
<div class="abs fcol" style="left:716px;width:105px">
  <h5>My Account</h5>
  <ul><li>My Orders</li><li>My Credit Slips</li><li>My Addresses</li><li>My Personal Info</li><li>My Vouchers</li><li>Hot Deals</li></ul>
</div>
<div class="abs fcol" style="left:864px;width:204px">
  <h5>Subscribe Us</h5>
  <div class="subscribe-box"><span>Your email address</span><b>GO</b></div>
  <p class="note">Sunday when we are open from and dions contact page.</p>
  <h5 style="border:0;margin:14px 0 0;padding:0">Get Social</h5>
  <div class="socials"><i></i><i></i><i></i><i></i><i></i></div>
</div>

<!-- bottom bar -->
<div class="abs bottom"></div>
<div class="abs copy">© Copyright 2014 Harbourly. All Right Reserved</div>
<div class="abs cards"><i></i><i></i><i></i><i></i><i></i></div>

</body>
</html>
```